Business Cards

Business card design for my company.
I would like the card's background colour to be black. You can also see our web site to get an idea of our brand. https://www.tmwhomecrafting.com.au/
- Name
- Email

```html
<!DOCTYPE html>
<html lang="en">
<head>
<meta charset="utf-8">
<title>TMW Home Crafting – Business Cards</title>
<link rel="stylesheet" href="https://fonts.googleapis.com/css2?family=Nunito+Sans:wght@400;600;700&display=swap">
<style>
  :root {
    --backdrop: #2e2e2e;
    --card: #141414;
    --white: #ffffff;
    --soft-white: #d9d9d9;
    --accent: #2fa84f;
    --muted-mark: #3c3c3c;
    --rule: #bdbdbd;
  }
  * { margin: 0; padding: 0; box-sizing: border-box; }
  html, body {
    width: 1200px;
    height: 1153px;
    overflow: hidden;
    background: var(--backdrop);
    font-family: "Nunito Sans", sans-serif;
  }
  .canvas { position: relative; width: 1200px; height: 1153px; }
  .card {
    position: absolute;
    left: 204px;
    width: 796px;
    background: var(--card);
    border-radius: 24px;
    box-shadow: 0 14px 30px rgba(0,0,0,0.55);
  }
  .card--front { top: 102px; height: 431px; }
  .card--back { top: 582px; height: 438px; }

  .brand-name {
    position: absolute;
    font-weight: 700;
    color: var(--white);
    line-height: 1.1;
    letter-spacing: 1px;
  }
  .card--front .brand-name {
    left: 118px;
    top: 150px;
    width: 260px;
    font-size: 40px;
    text-align: center;
  }
  .card--back .brand-name {
    left: 0;
    right: 0;
    top: 185px;
    font-size: 56px;
    text-align: center;
    color: var(--muted-mark);
  }

  .contact-block { position: absolute; left: 445px; top: 150px; width: 292px; }
  .person-name { font-size: 29px; font-weight: 400; color: var(--white); line-height: 1.1; }
  .person-role { font-size: 15px; color: var(--soft-white); margin-top: 2px; }
  .divider { height: 1px; background: var(--rule); margin: 22px 0 16px; width: 290px; }
  .contact-list { list-style: none; }
  .contact-list li {
    display: flex;
    align-items: center;
    gap: 12px;
    font-size: 16px;
    color: var(--soft-white);
    line-height: 23.5px;
  }
  .contact-list svg { width: 12px; height: 12px; fill: var(--accent); flex: none; }
</style>
</head>
<body>
<div class="canvas">
  <section class="card card--front">
    <div class="brand-name">TMW Home Crafting</div>
    <div class="contact-block">
      <div class="person-name">Neil Harper</div>
      <div class="person-role">General Manager</div>
      <div class="divider"></div>
      <ul class="contact-list">
        <li>
          <svg viewBox="0 0 24 24" aria-hidden="true"><path d="M6.6 10.8a15.1 15.1 0 0 0 6.6 6.6l2.2-2.2a1 1 0 0 1 1-.25 11.4 11.4 0 0 0 3.6.57 1 1 0 0 1 1 1V20a1 1 0 0 1-1 1A17 17 0 0 1 3 4a1 1 0 0 1 1-1h3.5a1 1 0 0 1 1 1c0 1.25.2 2.45.57 3.6a1 1 0 0 1-.25 1z"/></svg>
          0400 123 456
        </li>
        <li>
          <svg viewBox="0 0 24 24" aria-hidden="true"><path d="M2 5h20v14H2z"/></svg>
          info@tmwhomecrafting.com.au
        </li>
        <li>
          <svg viewBox="0 0 24 24" aria-hidden="true"><path d="M12 2a7 7 0 0 0-7 7c0 5.2 7 13 7 13s7-7.8 7-13a7 7 0 0 0-7-7zm0 9.5A2.5 2.5 0 1 1 12 6.5a2.5 2.5 0 0 1 0 5z"/></svg>
          Devonport, Tasmania, Australia
        </li>
      </ul>
    </div>
  </section>

  <section class="card card--back">
    <div class="brand-name">TMW Home Crafting</div>
  </section>
</div>
</body>
</html>
```